Business Card Design Project

We need a business card design for a relatively new company called Lumen Stride. We design paddle (an outdoor winter sport primarily played in the midwest and east coast) and tennis bags for women and men. Lumen Stride is a lifestyle brand for the next generation country club goers. Our bags merge fashion with functionality and are making country club sports trendier and more fashionable.

I would like to include space for
Name: (will fill this in for employees)
Lumen Stride
Phone: (will do this)
Email:
www.lumenstride-example.net

Would also like to include Facebook and Twitter icons.
Please do not use pictures of the bags - this is just to give you an idea of what style bags we sell.

Target Market(s)

30 to 40 year old men and women - luxury market

Industry/Entity Type

Fashion

Requirements
Must have
• Would like the company logo included

```html
<!DOCTYPE html>
<html lang="en">
<head>
<meta charset="utf-8">
<title>Lumen Stride — Business Card</title>
<link href="https://fonts.googleapis.com/css2?family=Josefin+Sans:wght@300&display=swap" rel="stylesheet">
<style>
  :root {
    --paper: #ffffff;
    --card-deep: #0c0c0c;
    --card-mid: #2a2a2a;
    --band-grey: #a7a7a9;
    --band-edge: #8f8f92;
    --mark-grey: #9c9c9e;
    --wordmark: #ffffff;
  }
  html, body {
    margin: 0;
    padding: 0;
    width: 1200px;
    height: 705px;
    overflow: hidden;
    background: var(--paper);
  }
  .card {
    position: relative;
    width: 1200px;
    height: 705px;
    overflow: hidden;
    background: radial-gradient(ellipse 70% 80% at 48% 52%, var(--card-mid) 0%, #1a1a1a 45%, var(--card-deep) 100%);
  }
  .card__bands {
    position: absolute;
    inset: 0;
    width: 1200px;
    height: 705px;
  }
  .brand {
    position: absolute;
    left: 78px;
    top: 258px;
    display: flex;
    align-items: center;
    gap: 48px;
  }
  .brand__dot {
    width: 112px;
    height: 112px;
    border-radius: 50%;
    background: var(--mark-grey);
    flex: none;
  }
  .brand__name {
    margin: 0;
    font-family: "Josefin Sans", sans-serif;
    font-weight: 300;
    font-size: 150px;
    line-height: 1;
    letter-spacing: 1px;
    color: var(--wordmark);
    white-space: nowrap;
    padding-top: 28px;
  }
</style>
</head>
<body>
  <main class="card">
    <svg class="card__bands" viewBox="0 0 1200 705" aria-hidden="true">
      <path d="M0 0 H1200 V58 Q600 88 0 58 Z" fill="var(--band-grey)" stroke="var(--band-edge)" stroke-width="2"/>
      <path d="M0 705 H1200 V650 Q600 618 0 650 Z" fill="var(--band-grey)" stroke="var(--band-edge)" stroke-width="2"/>
      <rect x="1" y="1" width="1198" height="703" fill="none" stroke="var(--band-edge)" stroke-width="2"/>
    </svg>
    <div class="brand">
      <span class="brand__dot" aria-hidden="true"></span>
      <h1 class="brand__name">Lumen Stride</h1>
    </div>
  </main>
</body>
</html>
```